Chat Software Business Card Design

We need a business card design for our company.

We provide businesses with a platform to communicate with their web visitors in real time using chat boxes on their web sites.

We're using a bright color scheme to attract attention on the site and the business card would do well to reflect this also to maintain brand awareness. However it is not essential to the ultimate design to use the same color scheme or feel as the site.

We offer a Free Trial of the software and would encourage a business card design to promote this if possible.

http://qelmarworks7.co.uk/projects/guest/index2.html

You will find the company logo attached also.

An eye catching design with something that will set the card apart from others is required.

The design of the card/theme of the card should be very unique, setting our selves apart, eye catching whilst not providing a "wacky" image for the company.

It should also include our contact information;~
Website - www.talkpond-live.com
Email - support@talkpond-live.com
Twitter - @Talkpondlive

Industry/Entity Type

Software

Contact Information for Business Card

Web - www.talkpond-live.com
Email - office@talkpond-live.com
Skype - Talkpond.Live

Requirements
Must have
• Use of company logo is required.

```html
<!DOCTYPE html>
<html lang="en">
<head>
<meta charset="utf-8">
<title>Talkpond Live — Business Cards</title>
<link rel="stylesheet" href="https://fonts.googleapis.com/css2?family=Open+Sans:wght@300;400;700&display=swap">
<style>
  :root {
    --stage: #2b2b2b;
    --card-white: #ffffff;
    --card-white-edge: #ececec;
    --brand-red: #e4532c;
    --brand-red-deep: #b5391c;
    --brand-amber: #e9a447;
    --contact-ink: #e0703f;
    --tagline-ink: #e8a06a;
    --url-ink: #f6c3ad;
  }
  * { box-sizing: border-box; margin: 0; padding: 0; }
  html, body {
    width: 1200px;
    height: 900px;
    overflow: hidden;
    background: var(--stage);
    font-family: "Open Sans", Arial, sans-serif;
  }
  .stage {
    position: relative;
    width: 1200px;
    height: 900px;
  }
  .card {
    position: absolute;
    width: 580px;
    height: 330px;
    overflow: hidden;
  }
  .card--back {
    left: 70px;
    top: 80px;
    background: linear-gradient(135deg, var(--card-white) 55%, var(--card-white-edge));
  }
  .card--front {
    left: 550px;
    top: 490px;
    background: linear-gradient(135deg, var(--brand-red) 35%, var(--brand-red-deep));
  }
  .wordmark {
    position: absolute;
    display: flex;
    align-items: center;
    gap: 14px;
  }
  .wordmark__square {
    width: 40px;
    height: 40px;
    border-radius: 6px;
    background: var(--brand-amber);
  }
  .wordmark__name {
    font-weight: 700;
    font-size: 46px;
    letter-spacing: -0.5px;
    line-height: 1;
  }
  .card--back .wordmark { left: 70px; top: 100px; }
  .card--back .wordmark__name { color: var(--brand-red); }
  .card--front .wordmark { left: 50%; top: 118px; transform: translateX(-50%); white-space: nowrap; }
  .card--front .wordmark__name { color: var(--card-white); }
  .contact-list {
    position: absolute;
    left: 40px;
    bottom: 28px;
    list-style: none;
    font-weight: 300;
    font-size: 14px;
    line-height: 1.45;
    color: var(--contact-ink);
  }
  .tagline {
    position: absolute;
    right: 40px;
    top: 206px;
    font-weight: 300;
    font-size: 12px;
    color: var(--tagline-ink);
  }
  .front-url {
    position: absolute;
    left: 0;
    right: 0;
    bottom: 34px;
    text-align: center;
    font-weight: 400;
    font-size: 15px;
    letter-spacing: 0.5px;
    color: var(--url-ink);
  }
</style>
</head>
<body>
  <main class="stage">
    <section class="card card--back" aria-label="Card back">
      <div class="wordmark">
        <span class="wordmark__square"></span>
        <span class="wordmark__name">Talkpond Live</span>
      </div>
      <p class="tagline">"Because your customer matters"</p>
      <ul class="contact-list">
        <li>e-mail: support@talkpond-live.com</li>
        <li>twitter: @Talkpondlive</li>
        <li>skype: Talkpond.Live</li>
        <li>web url: www.talkpond-live.com</li>
      </ul>
    </section>
    <section class="card card--front" aria-label="Card front">
      <div class="wordmark">
        <span class="wordmark__square"></span>
        <span class="wordmark__name">Talkpond Live</span>
      </div>
      <p class="front-url">www.talkpond-live.com</p>
    </section>
  </main>
</body>
</html>
```